Business Card Design

We would like a business card that utilizes our current logo and keeps with the same feel - elegant and organic. Our farm isn't about mass production, it's about excellence, education, beautiful events and flowers - people, culture, and community.

Target Market(s)

Patrons to our farm who are interested in weddings, events, or our flowers and vegetables.

Contact Information for Business Card

Name, address, cell email (Danielle Hoskins, 2716 Wrenfield Rd, Larkmoor, CO 80947, cell 30.412.6638, email danielle@wrenfieldacres.com)

```html
<!DOCTYPE html>
<html lang="en">
<head>
<meta charset="utf-8">
<title>Wrenfield Acres – Business Card</title>
<link rel="stylesheet" href="https://fonts.googleapis.com/css2?family=Lato:wght@400;700&display=swap">
<style>
  :root{
    --page:#ffffff;
    --card-front:#ffffff;
    --card-back:#788a77;
    --sage:#6f846c;
    --sage-text:#7b8a78;
    --leaf:#6f8a6a;
    --leaf-faint:rgba(210,225,205,.35);
    --accent:#a8743c;
    --white:#ffffff;
  }
  *{margin:0;padding:0;box-sizing:border-box}
  html,body{width:1200px;height:2778px;overflow:hidden;background:var(--page)}
  body{position:relative;font-family:"Lato",Arial,sans-serif}

  .card{position:absolute;left:215px;width:810px;height:462px;overflow:hidden;
        box-shadow:0 18px 40px rgba(0,0,0,.28)}
  .card--front{top:1559px;background:var(--card-front)}
  .card--back{top:2137px;background:var(--card-back)}

  .frame{position:absolute;inset:0;width:100%;height:100%}

  .leaf{position:absolute;opacity:.85}
  .leaf--front-tl{left:0;top:0;width:125px;height:75px;
        background:radial-gradient(ellipse at 40% 45%,var(--leaf) 0%,rgba(111,138,106,.5) 55%,transparent 75%)}
  .leaf--front-br{right:0;bottom:0;width:210px;height:78px;
        background:radial-gradient(ellipse at 45% 50%,var(--leaf) 0%,rgba(111,138,106,.5) 50%,transparent 75%)}
  .leaf--back-tr{right:0;top:0;width:150px;height:80px;
        background:radial-gradient(ellipse at 55% 45%,var(--leaf-faint) 0%,transparent 72%)}
  .leaf--back-bl{left:0;bottom:0;width:210px;height:100px;
        background:radial-gradient(ellipse at 45% 55%,var(--leaf-faint) 0%,transparent 72%)}

  .brand{position:absolute;font-weight:400;letter-spacing:.06em;white-space:nowrap}
  .brand--front{left:171px;top:108px;font-size:34px;color:var(--sage)}
  .brand--back{left:0;right:0;top:205px;text-align:center;font-size:46px;color:var(--white)}

  .holder{position:absolute;left:171px;top:224px;font-size:20px;font-weight:700;
          letter-spacing:.08em;text-transform:uppercase;color:var(--sage)}

  .contact{position:absolute;left:171px;top:253px;list-style:none}
  .contact li{display:flex;align-items:center;height:31px;font-size:15.5px;color:var(--sage-text)}
  .contact svg{width:14px;height:14px;margin-right:17px;fill:var(--accent)}

  .back-email{position:absolute;left:0;right:0;top:367px;text-align:center;
              font-size:15px;color:var(--white)}
</style>
</head>
<body>

<section class="card card--front" aria-label="Card front">
  <div class="leaf leaf--front-tl" role="img" aria-label="Sketched green leafy sprig"></div>
  <div class="leaf leaf--front-br" role="img" aria-label="Sketched green leafy sprig"></div>

  <svg class="frame" viewBox="0 0 810 462" aria-hidden="true">
    <defs>
      <linearGradient id="fadeLeft" x1="1" x2="0" y1="0" y2="0">
        <stop offset="0" stop-color="#6f846c"/><stop offset="1" stop-color="#6f846c" stop-opacity="0"/>
      </linearGradient>
      <linearGradient id="fadeDown" x1="0" x2="0" y1="0" y2="1">
        <stop offset="0" stop-color="#6f846c"/><stop offset="1" stop-color="#6f846c" stop-opacity="0"/>
      </linearGradient>
      <linearGradient id="fadeRight" x1="0" x2="1" y1="0" y2="0">
        <stop offset="0" stop-color="#6f846c"/><stop offset="1" stop-color="#6f846c" stop-opacity="0"/>
      </linearGradient>
      <linearGradient id="fadeUp" x1="0" x2="0" y1="1" y2="0">
        <stop offset="0" stop-color="#6f846c"/><stop offset="1" stop-color="#6f846c" stop-opacity="0"/>
      </linearGradient>
    </defs>
    <rect x="576" y="80" width="155" height="1.4" fill="url(#fadeLeft)"/>
    <rect x="730" y="80" width="1.4" height="150" fill="url(#fadeDown)"/>
    <rect x="79" y="381" width="155" height="1.4" fill="url(#fadeRight)"/>
    <rect x="79" y="230" width="1.4" height="152" fill="url(#fadeUp)"/>
  </svg>

  <div class="brand brand--front">Wrenfield Acres</div>
  <div class="holder">Danielle Hoskins</div>

  <ul class="contact">
    <li><svg viewBox="0 0 24 24"><path d="M6.6 10.8a15.1 15.1 0 0 0 6.6 6.6l2.2-2.2a1 1 0 0 1 1-.25 11.4 11.4 0 0 0 3.6.6 1 1 0 0 1 1 1V20a1 1 0 0 1-1 1A17 17 0 0 1 3 4a1 1 0 0 1 1-1h3.5a1 1 0 0 1 1 1c0 1.25.2 2.45.57 3.57a1 1 0 0 1-.25 1z"/></svg>30.412.6638</li>
    <li><svg viewBox="0 0 24 24"><path d="M12 2a7 7 0 0 0-7 7c0 5.25 7 13 7 13s7-7.75 7-13a7 7 0 0 0-7-7zm0 9.5A2.5 2.5 0 1 1 12 6.5a2.5 2.5 0 0 1 0 5z"/></svg>2716 Wrenfield Rd, Larkmoor, CO 80947</li>
    <li><svg viewBox="0 0 24 24"><path d="M2 5h20v14H2z" fill="none" stroke="#a8743c" stroke-width="2"/><path d="M2 5l10 8 10-8" fill="none" stroke="#a8743c" stroke-width="2"/></svg>danielle@wrenfieldacres.com</li>
  </ul>
</section>

<section class="card card--back" aria-label="Card back">
  <div class="leaf leaf--back-tr" role="img" aria-label="Faint pale leafy sprig"></div>
  <div class="leaf leaf--back-bl" role="img" aria-label="Faint pale leafy sprig"></div>

  <svg class="frame" viewBox="0 0 810 462" aria-hidden="true">
    <defs>
      <linearGradient id="wRight" x1="0" x2="1"><stop offset="0" stop-color="#fff"/><stop offset="1" stop-color="#fff" stop-opacity="0"/></linearGradient>
      <linearGradient id="wDown" x1="0" x2="0" y1="0" y2="1"><stop offset="0" stop-color="#fff"/><stop offset="1" stop-color="#fff" stop-opacity="0"/></linearGradient>
      <linearGradient id="wLeft" x1="1" x2="0"><stop offset="0" stop-color="#fff"/><stop offset="1" stop-color="#fff" stop-opacity="0"/></linearGradient>
      <linearGradient id="wUp" x1="0" x2="0" y1="1" y2="0"><stop offset="0" stop-color="#fff"/><stop offset="1" stop-color="#fff" stop-opacity="0"/></linearGradient>
    </defs>
    <rect x="79" y="80" width="155" height="1.4" fill="url(#wRight)"/>
    <rect x="79" y="80" width="1.4" height="170" fill="url(#wDown)"/>
    <rect x="578" y="381" width="151" height="1.4" fill="url(#wLeft)"/>
    <rect x="728" y="230" width="1.4" height="152" fill="url(#wUp)"/>
  </svg>

  <div class="brand brand--back">Wrenfield Acres</div>
  <div class="back-email">danielle@wrenfieldacres.com</div>
</section>

</body>
</html>
```